Brochure Design Project

I need a presentation folder with two inside pages and a pocket on back cover, use use my logo ,
make the cover just using the logo (put it big and centered, then use the logo in the background to fill, read the brief and make it modern, stop trying to make it exactly like the picture I gave as sample please use your talent trust your self
I just uploaded text for presentation folder
Target Market(s)
Dr's offices and patients

```html
<!DOCTYPE html>
<html lang="en">
<head>
<meta charset="utf-8">
<title>CareWell Counseling – Presentation Folder</title>
<link href="https://fonts.googleapis.com/css2?family=Didact+Gothic&display=swap" rel="stylesheet">
<style>
  :root {
    --stage: #f3f0ea;
    --cream-light: #efe8d8;
    --cream-mid: #e2d6bd;
    --cream-dark: #c6b491;
    --brown: #5b3717;
    --brown-text: #6e4c2c;
    --ink-soft: #7a5a3a;
    --white: #ffffff;
  }
  * { box-sizing: border-box; margin: 0; padding: 0; }
  html, body { width: 1200px; height: 800px; overflow: hidden; }
  body {
    background: var(--stage);
    font-family: "Didact Gothic", sans-serif;
    color: var(--brown-text);
    position: relative;
  }
  .spread {
    position: absolute;
    top: 200px;
    width: 560px;
    height: 400px;
    display: flex;
    box-shadow: 0 14px 30px rgba(60,40,20,0.18);
  }
  .spread--outside { left: 20px; }
  .spread--inside { left: 620px; }
  .panel {
    position: relative;
    width: 280px;
    height: 400px;
    overflow: hidden;
    background: linear-gradient(180deg, var(--cream-light) 0%, var(--cream-mid) 55%, var(--cream-dark) 100%);
  }
  .panel + .panel { border-left: 1px solid rgba(110,76,44,0.15); }

  /* brand lockup */
  .brand {
    position: absolute;
    left: 0; right: 0;
    text-align: center;
  }
  .brand__name {
    display: inline-flex;
    align-items: center;
    gap: 6px;
    font-size: 19px;
    color: var(--brown);
    white-space: nowrap;
  }
  .brand__dot {
    width: 10px; height: 10px;
    border-radius: 50%;
    background: var(--brown);
  }
  .brand__tagline {
    display: block;
    margin-top: 3px;
    font-size: 8px;
    letter-spacing: 0.5px;
    color: var(--ink-soft);
  }

  /* back cover */
  .back-cover .brand { top: 70px; }
  .back-cover__intro {
    position: absolute;
    top: 140px; left: 40px; right: 40px;
    text-align: center;
    font-size: 7.5px;
    line-height: 1.35;
    color: var(--brown-text);
  }
  .back-cover__intro p + p { margin-top: 8px; }
  .back-cover__address {
    position: absolute;
    bottom: 38px; left: 0; right: 0;
    text-align: center;
    font-size: 6.5px;
    line-height: 1.4;
    color: var(--ink-soft);
  }
  .back-cover__address p + p { margin-top: 6px; }

  /* front cover: big centred name over a faint repeated name pattern */
  .name-pattern {
    position: absolute;
    inset: -6px -40px;
    display: flex;
    flex-direction: column;
    justify-content: space-between;
    opacity: 0.09;
    pointer-events: none;
  }
  .name-pattern__row {
    display: flex;
    gap: 18px;
    white-space: nowrap;
    font-size: 13px;
    color: var(--brown);
  }
  .name-pattern__row:nth-child(even) { margin-left: -70px; }
  .name-pattern__item {
    display: inline-flex;
    align-items: center;
    gap: 4px;
  }
  .name-pattern__item::before {
    content: "";
    width: 7px; height: 7px;
    border-radius: 50%;
    background: var(--brown);
  }
  .cover-mark {
    position: absolute;
    left: 0; right: 0; top: 50%;
    transform: translateY(-50%);
    text-align: center;
  }
  .cover-mark__dot {
    display: block;
    width: 34px; height: 34px;
    margin: 0 auto 14px;
    border-radius: 50%;
    background: var(--brown);
  }
  .cover-mark__name {
    display: block;
    font-size: 36px;
    line-height: 1.05;
    color: var(--brown);
  }
  .cover-mark__tagline {
    display: block;
    margin-top: 10px;
    font-size: 10px;
    letter-spacing: 1px;
    color: var(--ink-soft);
  }

  /* inside left */
  .inside-left__services {
    position: absolute;
    top: 50px; left: 34px; right: 30px;
    font-size: 8px;
    line-height: 1.45;
    color: var(--brown-text);
  }
  .service-title {
    font-size: 10px;
    font-weight: 400;
    color: var(--brown);
    margin-top: 12px;
  }
  .service-title:first-child { margin-top: 0; }
  .service-list { list-style: none; margin-top: 3px; }
  .service-list li { padding-left: 9px; position: relative; }
  .service-list li::before {
    content: "";
    position: absolute;
    left: 0; top: 5px;
    width: 3px; height: 3px;
    border-radius: 50%;
    background: var(--brown-text);
  }

  /* inside right with pocket */
  .pocket {
    position: absolute;
    top: 0; bottom: 0; left: 52px; right: 0;
    background: var(--brown);
  }
  .pocket__notch {
    position: absolute;
    left: 22px; top: 88px;
    width: 60px; height: 60px;
    border-radius: 50%;
    background: var(--cream-mid);
  }
  .pocket__message {
    position: absolute;
    left: 72px; right: 14px; bottom: 60px;
    color: var(--white);
    font-size: 10px;
    line-height: 1.3;
  }
  .pocket__message p + p { margin-top: 10px; }
</style>
</head>
<body>

  <section class="spread spread--outside">
    <div class="panel back-cover">
      <div class="brand">
        <span class="brand__name"><span class="brand__dot"></span>CareWell Counseling</span>
        <span class="brand__tagline">a pro active addiction center</span>
      </div>
      <div class="back-cover__intro">
        <p>CareWell's Dedicated Counselors exude a contagious interest in the life of our patients, within an intimately scaled caring environment that engenders transformative learning.</p>
        <p>We're dedicated to informing and educating lives where every patient is treated as a person with individual needs by professional, caring staff.</p>
      </div>
      <div class="back-cover__address">
        <p>1820 Meadow Lane Road<br>Ashford, TX 75210</p>
        <p>Mailing Address<br>P.O. Box 482<br>Ashford, TX 75210</p>
        <p>555-014-2290 or 555-018-7731</p>
      </div>
    </div>

    <div class="panel front-cover">
      <div class="name-pattern" aria-hidden="true">
        <div class="name-pattern__row"><span class="name-pattern__item">CareWell</span><span class="name-pattern__item">CareWell</span><span class="name-pattern__item">CareWell</span><span class="name-pattern__item">CareWell</span></div>
        <div class="name-pattern__row"><span class="name-pattern__item">CareWell</span><span class="name-pattern__item">CareWell</span><span class="name-pattern__item">CareWell</span><span class="name-pattern__item">CareWell</span></div>
        <div class="name-pattern__row"><span class="name-pattern__item">CareWell</span><span class="name-pattern__item">CareWell</span><span class="name-pattern__item">CareWell</span><span class="name-pattern__item">CareWell</span></div>
        <div class="name-pattern__row"><span class="name-pattern__item">CareWell</span><span class="name-pattern__item">CareWell</span><span class="name-pattern__item">CareWell</span><span class="name-pattern__item">CareWell</span></div>
        <div class="name-pattern__row"><span class="name-pattern__item">CareWell</span><span class="name-pattern__item">CareWell</span><span class="name-pattern__item">CareWell</span><span class="name-pattern__item">CareWell</span></div>
        <div class="name-pattern__row"><span class="name-pattern__item">CareWell</span><span class="name-pattern__item">CareWell</span><span class="name-pattern__item">CareWell</span><span class="name-pattern__item">CareWell</span></div>
        <div class="name-pattern__row"><span class="name-pattern__item">CareWell</span><span class="name-pattern__item">CareWell</span><span class="name-pattern__item">CareWell</span><span class="name-pattern__item">CareWell</span></div>
        <div class="name-pattern__row"><span class="name-pattern__item">CareWell</span><span class="name-pattern__item">CareWell</span><span class="name-pattern__item">CareWell</span><span class="name-pattern__item">CareWell</span></div>
        <div class="name-pattern__row"><span class="name-pattern__item">CareWell</span><span class="name-pattern__item">CareWell</span><span class="name-pattern__item">CareWell</span><span class="name-pattern__item">CareWell</span></div>
        <div class="name-pattern__row"><span class="name-pattern__item">CareWell</span><span class="name-pattern__item">CareWell</span><span class="name-pattern__item">CareWell</span><span class="name-pattern__item">CareWell</span></div>
        <div class="name-pattern__row"><span class="name-pattern__item">CareWell</span><span class="name-pattern__item">CareWell</span><span class="name-pattern__item">CareWell</span><span class="name-pattern__item">CareWell</span></div>
        <div class="name-pattern__row"><span class="name-pattern__item">CareWell</span><span class="name-pattern__item">CareWell</span><span class="name-pattern__item">CareWell</span><span class="name-pattern__item">CareWell</span></div>
        <div class="name-pattern__row"><span class="name-pattern__item">CareWell</span><span class="name-pattern__item">CareWell</span><span class="name-pattern__item">CareWell</span><span class="name-pattern__item">CareWell</span></div>
        <div class="name-pattern__row"><span class="name-pattern__item">CareWell</span><span class="name-pattern__item">CareWell</span><span class="name-pattern__item">CareWell</span><span class="name-pattern__item">CareWell</span></div>
      </div>
      <div class="cover-mark">
        <span class="cover-mark__dot"></span>
        <span class="cover-mark__name">CareWell<br>Counseling</span>
        <span class="cover-mark__tagline">a pro active addiction center</span>
      </div>
    </div>
  </section>

  <section class="spread spread--inside">
    <div class="panel inside-left">
      <div class="inside-left__services">
        <h2 class="service-title">Patient Education</h2>
        <ul class="service-list">
          <li>Inform patients about taking medications inappropriately.</li>
          <li>Educate patients about signs and symptoms of substance use.</li>
        </ul>
        <h2 class="service-title">Screening for substance use disorders</h2>
        <ul class="service-list">
          <li>Treat substance use disorders related to prescribed medications</li>
          <li>Experienced staff to address substance use for patients taking pain medication</li>
        </ul>
        <h2 class="service-title">Pain Contracts</h2>
        <ul class="service-list">
          <li>Managing Pain Medication</li>
          <li>Storing Medication Safely</li>
        </ul>
      </div>
    </div>

    <div class="panel inside-right">
      <div class="pocket"></div>
      <div class="pocket__notch"></div>
      <div class="pocket__message">
        <p>According to the National Clinical Health Board more than 76 million Americans are suffering with chronic pain.</p>
        <p>Pro Active Addiction Counseling is needed and no one is providing this service!</p>
        <p>CareWell Counseling is !</p>
      </div>
    </div>
  </section>

</body>
</html>
```